Fernbrook premium pontoon cleaning and maintenance needs a business card design

we need a business card for a new company based in Brisbane and gold coast that offers to clean peoples pontoons using high pressure washers. The company name will be Fernbrook, and will offer premium pontoon cleaning and maintenance.
colours that can be used maybe black, lime green, grey, blue.but up for anything. cheers

Target Market(s)

people who own pontoons

Industry/Entity Type

Business

Contact Information for Business Card

contact
Rob Casworth
Duncan Pryle
mobile 0461 728 392
email Fernbrook@mailvista.net

Requirements
Nice to have
• like the look of black business cards the best

```html
<!DOCTYPE html>
<html lang="en">
<head>
<meta charset="utf-8">
<title>Fernbrook – Business Card</title>
<link href="https://fonts.googleapis.com/css2?family=Nunito:wght@800&family=Open+Sans:wght@400;600&display=swap" rel="stylesheet">
<style>
  :root {
    --page-bg: #e6e6e4;
    --card-dark: #2a2a2b;
    --lime: #d3e01c;
    --white: #f4f4f4;
    --grey-light: #c9c9c9;
    --grey-mid: #7a7a7a;
  }
  * { box-sizing: border-box; margin: 0; padding: 0; }
  html, body {
    width: 1200px; height: 1200px; overflow: hidden;
    background: var(--page-bg);
    font-family: "Open Sans", Arial, sans-serif;
  }
  .canvas { position: relative; width: 1200px; height: 1200px; }
  .card {
    position: absolute; left: 150px; width: 900px; height: 514px;
    background: var(--card-dark); overflow: hidden;
    box-shadow: 0 6px 18px rgba(0,0,0,.25);
  }
  .card--front { top: 60px; }
  .card--back { top: 626px; }

  .brand-name {
    font-family: "Nunito", "Trebuchet MS", sans-serif;
    font-weight: 800; color: var(--lime);
    font-size: 74px; line-height: 1; letter-spacing: 0.5px;
  }
  .tagline {
    color: var(--white); font-weight: 600;
    font-size: 14.5px; letter-spacing: 0.3px; text-transform: uppercase;
  }

  /* Front */
  .front-photo {
    position: absolute; left: 0; top: 0; width: 100%; height: 310px;
    background: linear-gradient(180deg, #8f8f90 0%, #b9b9b9 26%, #6d6d6e 40%, #4a4a4b 62%, var(--card-dark) 100%);
  }
  .card--front .brand-name { position: absolute; top: 222px; left: 0; width: 100%; text-align: center; }
  .card--front .tagline { position: absolute; top: 312px; left: 0; width: 100%; text-align: center; }
  .website {
    position: absolute; bottom: 26px; left: 0; width: 100%; text-align: center;
    color: var(--white); font-size: 16px;
  }

  /* Back */
  .back-photo {
    position: absolute; left: 0; top: 0; width: 600px; height: 100%;
    background:
      linear-gradient(90deg, rgba(42,42,43,0) 0%, rgba(42,42,43,0) 55%, var(--card-dark) 100%),
      linear-gradient(180deg, #a9a9a9 0%, #d0d0d0 28%, #8a8a8a 36%, #b7b7b7 58%, #6f6f70 78%, #3b3b3c 100%);
  }
  .card--back .brand-name { position: absolute; top: 92px; right: 70px; }
  .divider-line {
    position: absolute; top: 238px; left: 470px; right: 0; height: 6px;
    background: linear-gradient(90deg, rgba(200,200,200,0) 0%, var(--grey-mid) 35%, var(--grey-light) 100%);
  }
  .card--back .tagline { position: absolute; top: 252px; right: 28px; font-size: 13.5px; }
  .contact { position: absolute; left: 60px; top: 372px; }
  .contact-names { font-size: 26px; color: var(--lime); margin-bottom: 10px; }
  .contact-names .sep { color: var(--white); }
  .contact-line {
    display: flex; align-items: center; gap: 12px;
    color: var(--white); font-size: 18px; line-height: 28px;
  }
  .contact-line svg { width: 18px; height: 18px; flex: none; }
</style>
</head>
<body>
<div class="canvas">

  <section class="card card--front" aria-label="Card front">
    <div class="front-photo" role="img" aria-label="Black and white photograph of a calm lake at dusk with a jetty reaching into the water"></div>
    <h1 class="brand-name">Fernbrook</h1>
    <p class="tagline">Premium pontoon cleaning and maintenance.</p>
    <p class="website">www.Fernbrook.com.au</p>
  </section>

  <section class="card card--back" aria-label="Card back">
    <div class="back-photo" role="img" aria-label="Black and white photograph of a floating pontoon with pylons and a gangway on a river"></div>
    <h2 class="brand-name">Fernbrook</h2>
    <div class="divider-line"></div>
    <p class="tagline">Premium pontoon cleaning and maintenance.</p>
    <div class="contact">
      <p class="contact-names">Rob Casworth <span class="sep">/</span> Duncan Pryle</p>
      <p class="contact-line">
        <svg viewBox="0 0 18 18" aria-hidden="true"><rect x="4" y="1" width="10" height="16" rx="2" fill="none" stroke="#d3e01c" stroke-width="2"/><rect x="6.5" y="4" width="5" height="7" fill="#d3e01c"/></svg>
        0461 728 392
      </p>
      <p class="contact-line">
        <svg viewBox="0 0 18 18" aria-hidden="true"><rect x="1" y="3" width="16" height="12" fill="#d3e01c"/><path d="M1 3 L9 10 L17 3" fill="none" stroke="#2a2a2b" stroke-width="1.6"/></svg>
        Fernbrook@mailvista.net
      </p>
    </div>
  </section>

</div>
</body>
</html>
```